Calendar design with baby pictures

I need to get 2 calendars designed, one wall hanging A5 size and one table top. I want to use my baby pics on it in very creative way. On some months i just want to use one picture and on some i will want to use a collage of few pics. The design should allow me to place pictures myself later on as i dont want to upload so many pics here.

Baby

```html
<!DOCTYPE html>
<html lang="en">
<head>
<meta charset="utf-8">
<title>Baby Wall Calendar 2026</title>
<link href="https://fonts.googleapis.com/css2?family=Playball&family=Source+Sans+3:wght@400&display=swap" rel="stylesheet">
<style>
  :root {
    --canvas: #ffffff;
    --arch: #ffffff;
    --title: #e1b45c;
    --sunday: #e8846c;
    --digits: #6b6b6b;
    --caption: #2f2f2f;
    --photo: #8c7468;
    --jan: #8fc8ee;
    --feb: #d9eac4;
    --mar: #f4ae8f;
    --apr: #e3b4d8;
    --may: #cf9ca4;
    --jun: #50c0b9;
    --jul: #13b27b;
    --aug: #6a9a4f;
    --sep: #85a3a0;
    --oct: #f5d77b;
    --nov: #d3d3d3;
    --dec: #cc8087;
  }
  * { margin: 0; padding: 0; box-sizing: border-box; }
  html, body { width: 846px; height: 1200px; overflow: hidden; background: var(--canvas); }
  .canvas { position: relative; width: 846px; height: 1200px; font-family: "Source Sans 3", sans-serif; }

  .month-page {
    position: absolute;
    width: 503px; height: 714px;
    background: var(--page-bg);
    overflow: hidden;
  }
  .month-page .arch {
    position: absolute; left: 19px; top: 84px;
    width: 465px; height: 640px;
    background: var(--arch);
    border-radius: 232px 232px 0 0;
  }
  .month-page .sun-ring {
    position: absolute; left: 115px; top: 98px;
    width: 274px; height: 274px; border-radius: 50%;
    background: radial-gradient(circle closest-side,
      var(--arch) 0 70%,
      var(--ray-1) 72%,
      var(--ray-2) 84%,
      var(--ray-3) 94%,
      var(--arch) 100%);
    opacity: var(--ray-strength, .55);
  }
  .month-page .photo-slot {
    position: absolute; left: 157px; top: 140px;
    width: 190px; height: 190px; border-radius: 50%;
    background: var(--photo);
  }
  .month-page .month-name {
    position: absolute; left: 0; right: 0; top: 398px;
    text-align: center;
    font-family: "Playball", cursive;
    font-weight: 400;
    font-size: 56px; line-height: 1;
    color: var(--title);
  }
  .month-page .weekdays,
  .month-page .days {
    position: absolute; left: 101px; width: 307px;
    display: grid; grid-template-columns: repeat(7, 1fr);
    list-style: none;
    font-size: 25px; color: var(--digits);
    text-align: center;
  }
  .month-page .weekdays { top: 470px; line-height: 32px; }
  .month-page .days { top: 514px; grid-auto-rows: 35px; line-height: 35px; }
  .month-page .weekdays li:first-child,
  .month-page .days li:nth-child(7n+1) { color: var(--sunday); }

  .feature { left: 171px; top: 16px; }

  .caption {
    position: absolute; left: 0; right: 0; top: 746px;
    text-align: center; font-size: 19.5px; color: var(--caption);
  }

  .thumb { position: absolute; width: 137px; height: 195px; overflow: hidden; }
  .thumb .month-page { left: 0; top: 0; transform: scale(0.2727); transform-origin: 0 0; }
  .row-one { top: 788px; }
  .row-two { top: 997px; }
  .col-1 { left: 0; } .col-2 { left: 142px; } .col-3 { left: 283px; }
  .col-4 { left: 425px; } .col-5 { left: 567px; } .col-6 { left: 709px; }

  .jan { --page-bg: var(--jan); --ray-1: #e7bd6a; --ray-2: #e58a4e; --ray-3: #b8384f; --ray-strength: .75; }
  .feb { --page-bg: var(--feb); --ray-1: #f2c98a; --ray-2: #f0a36a; --ray-3: #f2c98a; --ray-strength: .6; }
  .mar { --page-bg: var(--mar); --ray-1: #f4b08e; --ray-2: #e98f6e; --ray-3: #f6c7b0; --ray-strength: .6; }
  .apr { --page-bg: var(--apr); --ray-1: #e8a25c; --ray-2: #c9455a; --ray-3: #f1c36e; --ray-strength: .55; }
  .may { --page-bg: var(--may); --ray-1: #e6ad5a; --ray-2: #b8384f; --ray-3: #e58a4e; --ray-strength: .55; }
  .jun { --page-bg: var(--jun); --ray-1: #f0c070; --ray-2: #c4405a; --ray-3: #e58a4e; --ray-strength: .6; }
  .jul { --page-bg: var(--jul); --ray-1: #f3cd6b; --ray-2: #e29a5c; --ray-3: #d27a8a; --ray-strength: .8; }
  .aug { --page-bg: var(--aug); --ray-1: #b8384f; --ray-2: #e58a4e; --ray-3: #e7bd6a; --ray-strength: .7; }
  .sep { --page-bg: var(--sep); --ray-1: #e7bd6a; --ray-2: #c05a5a; --ray-3: #e58a4e; --ray-strength: .6; }
  .oct { --page-bg: var(--oct); --ray-1: #e58a4e; --ray-2: #b8384f; --ray-3: #e7bd6a; --ray-strength: .8; }
  .nov { --page-bg: var(--nov); --ray-1: #f0a050; --ray-2: #e8763e; --ray-3: #f3c87a; --ray-strength: .6; }
  .dec { --page-bg: var(--dec); --ray-1: #e7bd6a; --ray-2: #c4405a; --ray-3: #e58a4e; --ray-strength: .6; }
</style>
</head>
<body>
<main class="canvas">

  <section class="month-page feature jan">
    <div class="arch"></div>
    <div class="sun-ring" role="img" aria-label="Sun-ray ornament in orange, berry and gold around the photo"></div>
    <div class="photo-slot" role="img" aria-label="Round baby photo placeholder"></div>
    <h1 class="month-name">January</h1>
    <ul class="weekdays"><li>S</li><li>M</li><li>T</li><li>W</li><li>T</li><li>F</li><li>S</li></ul>
    <ul class="days"><li></li><li></li><li></li><li></li><li>1</li><li>2</li><li>3</li><li>4</li><li>5</li><li>6</li><li>7</li><li>8</li><li>9</li><li>10</li><li>11</li><li>12</li><li>13</li><li>14</li><li>15</li><li>16</li><li>17</li><li>18</li><li>19</li><li>20</li><li>21</li><li>22</li><li>23</li><li>24</li><li>25</li><li>26</li><li>27</li><li>28</li><li>29</li><li>30</li><li>31</li></ul>
  </section>

  <p class="caption">12 months / Wall Calendar (12 pages) / Every different pic for each month</p>

  <div class="thumb row-one col-1"><section class="month-page jan"><div class="arch"></div><div class="sun-ring" role="img" aria-label="Sun-ray ornament"></div><div class="photo-slot" role="img" aria-label="Baby photo placeholder"></div><h2 class="month-name">January</h2><ul class="weekdays"><li>S</li><li>M</li><li>T</li><li>W</li><li>T</li><li>F</li><li>S</li></ul><ul class="days"><li></li><li></li><li></li><li></li><li>1</li><li>2</li><li>3</li><li>4</li><li>5</li><li>6</li><li>7</li><li>8</li><li>9</li><li>10</li><li>11</li><li>12</li><li>13</li><li>14</li><li>15</li><li>16</li><li>17</li><li>18</li><li>19</li><li>20</li><li>21</li><li>22</li><li>23</li><li>24</li><li>25</li><li>26</li><li>27</li><li>28</li><li>29</li><li>30</li><li>31</li></ul></section></div>

  <div class="thumb row-one col-2"><section class="month-page feb"><div class="arch"></div><div class="sun-ring" role="img" aria-label="Fine sun-ray ornament"></div><div class="photo-slot" role="img" aria-label="Baby photo placeholder"></div><h2 class="month-name">February</h2><ul class="weekdays"><li>S</li><li>M</li><li>T</li><li>W</li><li>T</li><li>F</li><li>S</li></ul><ul class="days"><li>1</li><li>2</li><li>3</li><li>4</li><li>5</li><li>6</li><li>7</li><li>8</li><li>9</li><li>10</li><li>11</li><li>12</li><li>13</li><li>14</li><li>15</li><li>16</li><li>17</li><li>18</li><li>19</li><li>20</li><li>21</li><li>22</li><li>23</li><li>24</li><li>25</li><li>26</li><li>27</li><li>28</li></ul></section></div>

  <div class="thumb row-one col-3"><section class="month-page mar"><div class="arch"></div><div class="sun-ring" role="img" aria-label="Droplet ray ornament"></div><div class="photo-slot" role="img" aria-label="Baby photo placeholder"></div><h2 class="month-name">March</h2><ul class="weekdays"><li>S</li><li>M</li><li>T</li><li>W</li><li>T</li><li>F</li><li>S</li></ul><ul class="days"><li>1</li><li>2</li><li>3</li><li>4</li><li>5</li><li>6</li><li>7</li><li>8</li><li>9</li><li>10</li><li>11</li><li>12</li><li>13</li><li>14</li><li>15</li><li>16</li><li>17</li><li>18</li><li>19</li><li>20</li><li>21</li><li>22</li><li>23</li><li>24</li><li>25</li><li>26</li><li>27</li><li>28</li><li>29</li><li>30</li><li>31</li></ul></section></div>

  <div class="thumb row-one col-4"><section class="month-page apr"><div class="arch"></div><div class="sun-ring" role="img" aria-label="Triangle ray ornament"></div><div class="photo-slot" role="img" aria-label="Baby photo placeholder"></div><h2 class="month-name">April</h2><ul class="weekdays"><li>S</li><li>M</li><li>T</li><li>W</li><li>T</li><li>F</li><li>S</li></ul><ul class="days"><li></li><li></li><li></li><li>1</li><li>2</li><li>3</li><li>4</li><li>5</li><li>6</li><li>7</li><li>8</li><li>9</li><li>10</li><li>11</li><li>12</li><li>13</li><li>14</li><li>15</li><li>16</li><li>17</li><li>18</li><li>19</li><li>20</li><li>21</li><li>22</li><li>23</li><li>24</li><li>25</li><li>26</li><li>27</li><li>28</li><li>29</li><li>30</li></ul></section></div>

  <div class="thumb row-one col-5"><section class="month-page may"><div class="arch"></div><div class="sun-ring" role="img" aria-label="Leaf ray ornament"></div><div class="photo-slot" role="img" aria-label="Baby photo placeholder"></div><h2 class="month-name">May</h2><ul class="weekdays"><li>S</li><li>M</li><li>T</li><li>W</li><li>T</li><li>F</li><li>S</li></ul><ul class="days"><li>31</li><li></li><li></li><li></li><li></li><li>1</li><li>2</li><li>3</li><li>4</li><li>5</li><li>6</li><li>7</li><li>8</li><li>9</li><li>10</li><li>11</li><li>12</li><li>13</li><li>14</li><li>15</li><li>16</li><li>17</li><li>18</li><li>19</li><li>20</li><li>21</li><li>22</li><li>23</li><li>24</li><li>25</li><li>26</li><li>27</li><li>28</li><li>29</li><li>30</li></ul></section></div>

  <div class="thumb row-one col-6"><section class="month-page jun"><div class="arch"></div><div class="sun-ring" role="img" aria-label="Teardrop ray ornament"></div><div class="photo-slot" role="img" aria-label="Baby photo placeholder"></div><h2 class="month-name">June</h2><ul class="weekdays"><li>S</li><li>M</li><li>T</li><li>W</li><li>T</li><li>F</li><li>S</li></ul><ul class="days"><li></li><li>1</li><li>2</li><li>3</li><li>4</li><li>5</li><li>6</li><li>7</li><li>8</li><li>9</li><li>10</li><li>11</li><li>12</li><li>13</li><li>14</li><li>15</li><li>16</li><li>17</li><li>18</li><li>19</li><li>20</li><li>21</li><li>22</li><li>23</li><li>24</li><li>25</li><li>26</li><li>27</li><li>28</li><li>29</li><li>30</li></ul></section></div>

  <div class="thumb row-two col-1"><section class="month-page jul"><div class="arch"></div><div class="sun-ring" role="img" aria-label="Petal ray ornament"></div><div class="photo-slot" role="img" aria-label="Baby photo placeholder"></div><h2 class="month-name">July</h2><ul class="weekdays"><li>S</li><li>M</li><li>T</li><li>W</li><li>T</li><li>F</li><li>S</li></ul><ul class="days"><li></li><li></li><li></li><li>1</li><li>2</li><li>3</li><li>4</li><li>5</li><li>6</li><li>7</li><li>8</li><li>9</li><li>10</li><li>11</li><li>12</li><li>13</li><li>14</li><li>15</li><li>16</li><li>17</li><li>18</li><li>19</li><li>20</li><li>21</li><li>22</li><li>23</li><li>24</li><li>25</li><li>26</li><li>27</li><li>28</li><li>29</li><li>30</li><li>31</li></ul></section></div>

  <div class="thumb row-two col-2"><section class="month-page aug"><div class="arch"></div><div class="sun-ring" role="img" aria-label="Dense spike ray ornament"></div><div class="photo-slot" role="img" aria-label="Baby photo placeholder"></div><h2 class="month-name">August</h2><ul class="weekdays"><li>S</li><li>M</li><li>T</li><li>W</li><li>T</li><li>F</li><li>S</li></ul><ul class="days"><li>30</li><li>31</li><li></li><li></li><li></li><li></li><li>1</li><li>2</li><li>3</li><li>4</li><li>5</li><li>6</li><li>7</li><li>8</li><li>9</li><li>10</li><li>11</li><li>12</li><li>13</li><li>14</li><li>15</li><li>16</li><li>17</li><li>18</li><li>19</li><li>20</li><li>21</li><li>22</li><li>23</li><li>24</li><li>25</li><li>26</li><li>27</li><li>28</li><li>29</li></ul></section></div>

  <div class="thumb row-two col-3"><section class="month-page sep"><div class="arch"></div><div class="sun-ring" role="img" aria-label="Triangle ray ornament"></div><div class="photo-slot" role="img" aria-label="Baby photo placeholder"></div><h2 class="month-name">September</h2><ul class="weekdays"><li>S</li><li>M</li><li>T</li><li>W</li><li>T</li><li>F</li><li>S</li></ul><ul class="days"><li></li><li></li><li>1</li><li>2</li><li>3</li><li>4</li><li>5</li><li>6</li><li>7</li><li>8</li><li>9</li><li>10</li><li>11</li><li>12</li><li>13</li><li>14</li><li>15</li><li>16</li><li>17</li><li>18</li><li>19</li><li>20</li><li>21</li><li>22</li><li>23</li><li>24</li><li>25</li><li>26</li><li>27</li><li>28</li><li>29</li><li>30</li></ul></section></div>

  <div class="thumb row-two col-4"><section class="month-page oct"><div class="arch"></div><div class="sun-ring" role="img" aria-label="Bar ray ornament"></div><div class="photo-slot" role="img" aria-label="Baby photo placeholder"></div><h2 class="month-name">October</h2><ul class="weekdays"><li>S</li><li>M</li><li>T</li><li>W</li><li>T</li><li>F</li><li>S</li></ul><ul class="days"><li></li><li></li><li></li><li></li><li>1</li><li>2</li><li>3</li><li>4</li><li>5</li><li>6</li><li>7</li><li>8</li><li>9</li><li>10</li><li>11</li><li>12</li><li>13</li><li>14</li><li>15</li><li>16</li><li>17</li><li>18</li><li>19</li><li>20</li><li>21</li><li>22</li><li>23</li><li>24</li><li>25</li><li>26</li><li>27</li><li>28</li><li>29</li><li>30</li><li>31</li></ul></section></div>

  <div class="thumb row-two col-5"><section class="month-page nov"><div class="arch"></div><div class="sun-ring" role="img" aria-label="Line ray ornament"></div><div class="photo-slot" role="img" aria-label="Baby photo placeholder"></div><h2 class="month-name">November</h2><ul class="weekdays"><li>S</li><li>M</li><li>T</li><li>W</li><li>T</li><li>F</li><li>S</li></ul><ul class="days"><li>1</li><li>2</li><li>3</li><li>4</li><li>5</li><li>6</li><li>7</li><li>8</li><li>9</li><li>10</li><li>11</li><li>12</li><li>13</li><li>14</li><li>15</li><li>16</li><li>17</li><li>18</li><li>19</li><li>20</li><li>21</li><li>22</li><li>23</li><li>24</li><li>25</li><li>26</li><li>27</li><li>28</li><li>29</li><li>30</li></ul></section></div>

  <div class="thumb row-two col-6"><section class="month-page dec"><div class="arch"></div><div class="sun-ring" role="img" aria-label="Swirl ray ornament"></div><div class="photo-slot" role="img" aria-label="Baby photo placeholder"></div><h2 class="month-name">December</h2><ul class="weekdays"><li>S</li><li>M</li><li>T</li><li>W</li><li>T</li><li>F</li><li>S</li></ul><ul class="days"><li></li><li></li><li>1</li><li>2</li><li>3</li><li>4</li><li>5</li><li>6</li><li>7</li><li>8</li><li>9</li><li>10</li><li>11</li><li>12</li><li>13</li><li>14</li><li>15</li><li>16</li><li>17</li><li>18</li><li>19</li><li>20</li><li>21</li><li>22</li><li>23</li><li>24</li><li>25</li><li>26</li><li>27</li><li>28</li><li>29</li><li>30</li><li>31</li></ul></section></div>

</main>
</body>
</html>
```